Dential Clinic Business Card

We need a simple elegant business card. 2 sided. First side with our details, and 2nd side with appointment time rows.

Dark background preferred. Will consider monotone design, or colored. Surprise us.

Details:
SIDE1

Maplewood Square Dental

Dr Peter Hollis
BDSc(Adel) FRZPTA

Shop 42, Maplewood Square
7-19 Birch Parade, Lindenvale VIC 3189
Phone: 03 9555 0148
email: info@maplewoodsquaredental.com.au
site: www.maplewoodsquaredental.com.au
_____________________________________
SIDE 2
Appointed Time ________________________
Notes _______________________

Target Market(s)

Dental Patients

Industry/Entity Type

Healthcare

Contact Information for Business Card

SIDE1

Maplewood Square Dental

Dr Peter Hollis
Shop 42, Maplewood Square
Phone: 03 9555 0148
SIDE 2

Font styles to use
Other font styles liked:
• Comfortaa

Requirements
Must have
• Dr Peter Hollis
BDSc(Adel) FRZPTA

Address
Phone
Email
Website
Nice to have
• Simple elegant design with our logo.
Colored logo.
Light text on dark background - Side 1
Light background so can be written on with dark pen - SIde 2
Should not have
• Too many colors

```html
<!DOCTYPE html>
<html lang="en">
<head>
<meta charset="utf-8">
<title>Maplewood Square Dental – Business Card</title>
<link href="https://fonts.googleapis.com/css2?family=Questrial&display=swap" rel="stylesheet">
<style>
  :root {
    --page: #e6e7e9;
    --card-light: #ffffff;
    --card-dark: #221f20;
    --brand-blue: #1a9bd7;
    --brand-green: #7bc143;
    --ink: #1d1d1d;
    --text-light: #e9e9e9;
    --text-muted: #c9c9c9;
  }
  * { box-sizing: border-box; margin: 0; padding: 0; }
  html, body { width: 1200px; height: 965px; overflow: hidden; }
  body {
    background: var(--page);
    font-family: "Questrial", "Helvetica Neue", Arial, sans-serif;
    position: relative;
  }
  .card {
    position: absolute;
    left: 250px;
    width: 700px;
    height: 428px;
    overflow: hidden;
    box-shadow: 0 6px 18px rgba(0,0,0,.18);
  }
  .card-wave { position: absolute; inset: 0; width: 100%; height: 100%; }

  /* Appointment side */
  .card--appointment { top: 40px; background: var(--card-light); }
  .brand {
    position: absolute;
    display: flex;
    align-items: center;
    gap: 14px;
  }
  .brand-dot {
    width: 44px; height: 44px;
    border-radius: 50%;
    background: var(--brand-green);
    flex: none;
  }
  .brand-name {
    font-size: 30px;
    letter-spacing: .5px;
    color: var(--brand-blue);
    white-space: nowrap;
  }
  .card--appointment .brand { left: 36px; top: 38px; }
  .appointment-rows {
    position: absolute;
    left: 40px; right: 40px; top: 128px;
    list-style: none;
  }
  .appointment-row {
    display: flex;
    align-items: flex-end;
    gap: 10px;
    height: 42px;
  }
  .appointment-label {
    font-size: 19px;
    color: var(--brand-blue);
    letter-spacing: .5px;
    white-space: nowrap;
  }
  .appointment-line {
    flex: 1;
    border-bottom: 1.5px solid var(--ink);
    margin-bottom: 5px;
  }

  /* Details side */
  .card--details { top: 498px; background: var(--card-dark); }
  .card--details .brand { left: 34px; top: 205px; }
  .card--details .brand-dot { width: 36px; height: 36px; }
  .card--details .brand-name { font-size: 22px; }
  .details-divider {
    position: absolute;
    left: 376px; top: 54px;
    width: 2px; height: 200px;
    background: var(--brand-blue);
  }
  .details {
    position: absolute;
    left: 396px; top: 46px;
    color: var(--text-light);
  }
  .dentist-name {
    font-size: 28px;
    color: var(--brand-blue);
    letter-spacing: .3px;
    font-weight: 400;
  }
  .dentist-role {
    font-size: 15px;
    color: var(--text-muted);
    margin-top: 2px;
  }
  .address {
    font-style: normal;
    font-size: 15px;
    line-height: 1.35;
    margin-top: 16px;
  }
  .contacts {
    list-style: none;
    margin-top: 12px;
    font-size: 13.5px;
  }
  .contact {
    display: flex;
    align-items: center;
    gap: 9px;
    height: 22px;
    white-space: nowrap;
  }
  .contact-icon { width: 14px; height: 14px; flex: none; }
  .site-accent { color: var(--brand-green); }
  .site-blue { color: var(--brand-blue); }
</style>
</head>
<body>

<section class="card card--appointment" aria-label="Appointment side">
  <svg class="card-wave" viewBox="0 0 700 428" preserveAspectRatio="none" aria-hidden="true">
    <path d="M0,380 Q380,410 700,320 L700,428 L0,428 Z" fill="var(--brand-blue)"/>
    <path d="M0,390 Q380,420 700,332 L700,428 L0,428 Z" fill="var(--brand-green)"/>
  </svg>
  <div class="brand">
    <span class="brand-dot"></span>
    <span class="brand-name">Maplewood Square Dental</span>
  </div>
  <ul class="appointment-rows">
    <li class="appointment-row"><span class="appointment-label">APPOINTED TIME:</span><span class="appointment-line"></span></li>
    <li class="appointment-row"><span class="appointment-label">NOTES:</span><span class="appointment-line"></span></li>
    <li class="appointment-row"><span class="appointment-label">APPOINTED TIME:</span><span class="appointment-line"></span></li>
    <li class="appointment-row"><span class="appointment-label">NOTES:</span><span class="appointment-line"></span></li>
  </ul>
</section>

<section class="card card--details" aria-label="Details side">
  <svg class="card-wave" viewBox="0 0 700 428" preserveAspectRatio="none" aria-hidden="true">
    <path d="M0,362 Q380,385 700,290 L700,428 L0,428 Z" fill="var(--brand-blue)"/>
    <path d="M0,372 Q380,396 700,304 L700,428 L0,428 Z" fill="var(--brand-green)"/>
  </svg>
  <div class="brand">
    <span class="brand-dot"></span>
    <span class="brand-name">Maplewood Square Dental</span>
  </div>
  <span class="details-divider"></span>
  <div class="details">
    <h1 class="dentist-name">DR PETER HOLLIS</h1>
    <p class="dentist-role">Principal Dentist</p>
    <address class="address">
      Shop 42, Maplewood Square<br>
      7-19 Birch Parade, Lindenvale VIC 3189
    </address>
    <ul class="contacts">
      <li class="contact">
        <svg class="contact-icon" viewBox="0 0 16 16" aria-hidden="true"><path d="M4 1.5l2.2 3-1.4 1.6a9 9 0 0 0 5.1 5.1l1.6-1.4 3 2.2-1.3 2.3C7.5 14 2 8.5 1.7 2.8z" fill="none" stroke="var(--brand-green)" stroke-width="1.3" stroke-linejoin="round"/></svg>
        <span>03 9555 0148</span>
      </li>
      <li class="contact">
        <svg class="contact-icon" viewBox="0 0 16 16" aria-hidden="true"><rect x="1.5" y="3.5" width="13" height="9" fill="none" stroke="var(--brand-green)" stroke-width="1.3"/><path d="M1.5 3.5L8 9l6.5-5.5" fill="none" stroke="var(--brand-green)" stroke-width="1.3"/></svg>
        <span>info@maplewoodsquaredental.com.au</span>
      </li>
      <li class="contact">
        <svg class="contact-icon" viewBox="0 0 16 16" aria-hidden="true"><circle cx="8" cy="8" r="6.5" fill="var(--brand-green)"/><path d="M1.5 8h13M8 1.5c-3 3.5-3 9.5 0 13M8 1.5c3 3.5 3 9.5 0 13" fill="none" stroke="var(--card-dark)" stroke-width="1"/></svg>
        <span>www.<span class="site-blue">maplewood</span><span class="site-accent">squaredental</span>.com.au</span>
      </li>
    </ul>
  </div>
</section>

</body>
</html>
```